Premium Triple Sec liquor / spirits brand

This is a completely open opportunity to name and design a new-to-world brand and bottle label for a triple sec (orange-flavoured liqueur). It should have premium features, a modern style and is designed to be perfect for mixing into famous cocktails such as the Margarita, Cosmopolitan and Mai Tai. The industry reference for the category is Valmorette. If you don't want to create a name, please default to 'Drunavic'.

Target Market(s)

25-45yr olds interested in making cocktails at home (male and female)

Industry/Entity Type

Spirits / Liquor

Colors
FFC000
F8CF3A
FAE287
FDF2CF
FEFAEE
F0912C
F2A743
F7CA91
FBE8D2
FDF5EE
EE7325
F08F49
F5BC92
FAE3D3
FDF4ED

Requirements
Must have
• The liquid in any bottles must be clear.

```html
<!DOCTYPE html>
<html lang="en">
<head>
<meta charset="utf-8">
<title>Drunavic Triple Sec — Label Set</title>
<link rel="stylesheet" href="https://fonts.googleapis.com/css2?family=Exo+2:wght@600&family=Montserrat:ital,wght@0,300;0,600;1,300&family=Roboto:wght@400&family=Roboto+Condensed:wght@700&display=swap">
<style>
  :root {
    --bg: #eefbcb;
    --label-black: #1d1b1c;
    --gold: #ffcc00;
    --white: #ffffff;
    --dim-line: #4a4a4a;
  }
  * { margin: 0; padding: 0; box-sizing: border-box; }
  html, body { width: 968px; height: 1200px; overflow: hidden; }
  body {
    position: relative;
    background: radial-gradient(circle at 50% 50%, #f6fde4 0%, var(--bg) 70%);
    font-family: "Roboto", Arial, sans-serif;
  }
  .dimensions { position: absolute; left: 0; top: 0; }
  .dim-text { font-family: "Roboto Condensed", Arial, sans-serif; font-weight: 400; fill: var(--dim-line); }

  .neck-label { position: absolute; left: 131px; top: 100px; width: 706px; height: 176px; }
  .neck-name { font-family: "Exo 2", sans-serif; font-weight: 600; font-size: 34px; fill: var(--gold); }

  .front-label {
    position: absolute; left: 265px; top: 390px;
    width: 437px; height: 763px;
    background: var(--label-black);
    border-radius: 14px;
    color: var(--white);
    text-align: center;
  }
  .front-frame {
    position: absolute; inset: 17px;
    border: 4px solid var(--white);
    border-radius: 2px;
  }
  .front-label > p, .front-label > div.crest { position: absolute; left: 0; width: 100%; }
  .product-title {
    top: 38px; font-family: "Montserrat", sans-serif; font-weight: 600;
    font-size: 48px; letter-spacing: 4px; line-height: 1;
  }
  .product-title .accent { color: var(--gold); }
  .origin {
    top: 108px; font-family: "Montserrat", sans-serif; font-weight: 300;
    font-size: 19px; letter-spacing: 2px;
  }
  .crest {
    top: 168px; height: 270px;
  }
  .crest-ring {
    position: absolute; left: 83px; top: 0;
    width: 270px; height: 270px;
    border: 4px solid var(--gold); border-radius: 50%;
  }
  .crest-name {
    position: absolute; left: 0; width: 100%; top: 108px;
    font-family: "Exo 2", sans-serif; font-weight: 600; font-size: 44px;
    color: var(--gold); line-height: 1;
  }
  .vintage {
    top: 483px; font-family: "Roboto Condensed", sans-serif; font-weight: 700;
    font-size: 30px; line-height: 1;
  }
  .brand-name {
    top: 520px; font-family: "Exo 2", sans-serif; font-weight: 600;
    font-size: 60px; color: var(--gold); line-height: 1;
  }
  .descriptor {
    top: 586px; font-family: "Montserrat", sans-serif; font-style: italic; font-weight: 300;
    font-size: 17px;
  }
  .appellation { top: 640px; font-size: 17px; }
  .facts {
    position: absolute; left: 0; top: 702px; width: 100%;
    font-size: 15px;
  }
  .facts span { position: absolute; transform: translateX(-50%); white-space: nowrap; }
  .facts .abv { left: 94px; }
  .facts .style { left: 233px; }
  .facts .volume { left: 362px; }
</style>
</head>
<body>

<svg class="dimensions" width="968" height="1200" viewBox="0 0 968 1200" aria-hidden="true">
  <g stroke="var(--dim-line)" stroke-width="1" fill="none">
    <!-- neck label width -->
    <line x1="131" y1="78" x2="837" y2="78"/>
    <line x1="131" y1="64" x2="131" y2="92"/>
    <line x1="151" y1="64" x2="151" y2="92"/>
    <line x1="817" y1="64" x2="817" y2="92"/>
    <line x1="837" y1="64" x2="837" y2="92"/>
    <!-- neck label height -->
    <line x1="858" y1="100" x2="858" y2="276"/>
    <line x1="846" y1="100" x2="870" y2="100"/>
    <line x1="846" y1="276" x2="870" y2="276"/>
    <!-- front label width -->
    <line x1="265" y1="360" x2="702" y2="360"/>
    <line x1="265" y1="348" x2="265" y2="372"/>
    <line x1="702" y1="348" x2="702" y2="372"/>
    <!-- front label height -->
    <line x1="240" y1="390" x2="240" y2="1153"/>
    <line x1="228" y1="390" x2="252" y2="390"/>
    <line x1="228" y1="1153" x2="252" y2="1153"/>
  </g>
  <text class="dim-text" x="484" y="74" font-size="20" text-anchor="middle">4 Inch</text>
  <text class="dim-text" x="141" y="56" font-size="11" text-anchor="middle">0.2</text>
  <text class="dim-text" x="141" y="67" font-size="11" text-anchor="middle">Inch</text>
  <text class="dim-text" x="827" y="56" font-size="11" text-anchor="middle">0.2</text>
  <text class="dim-text" x="827" y="67" font-size="11" text-anchor="middle">Inch</text>
  <text class="dim-text" x="872" y="195" font-size="20">1 Inch</text>
  <text class="dim-text" x="484" y="354" font-size="20" text-anchor="middle">2.27 Inch</text>
  <text class="dim-text" font-size="20" text-anchor="middle" transform="translate(226 771) rotate(-90)">4.12 Inch</text>
</svg>

<svg class="neck-label" viewBox="0 0 706 176" role="group" aria-label="Neck label">
  <rect width="706" height="176" fill="var(--label-black)"/>
  <rect y="23" width="706" height="10" fill="var(--gold)"/>
  <rect y="145" width="706" height="10" fill="var(--gold)"/>
  <g fill="none" stroke="var(--gold)" stroke-width="2">
    <circle cx="157" cy="75" r="27"/>
    <circle cx="356" cy="75" r="27"/>
    <circle cx="554" cy="75" r="27"/>
  </g>
  <text class="neck-name" x="157" y="131" text-anchor="middle">Drunavic</text>
  <text class="neck-name" x="356" y="131" text-anchor="middle">Drunavic</text>
  <text class="neck-name" x="554" y="131" text-anchor="middle">Drunavic</text>
  <g stroke="var(--white)" stroke-width="2">
    <line x1="252" y1="106" x2="252" y2="134"/>
    <line x1="257" y1="106" x2="257" y2="134"/>
    <line x1="451" y1="106" x2="451" y2="134"/>
    <line x1="456" y1="106" x2="456" y2="134"/>
  </g>
</svg>

<section class="front-label" aria-label="Front label">
  <div class="front-frame"></div>
  <p class="product-title">Triple <span class="accent">Sec</span></p>
  <p class="origin">PRODUCT OF ITALY</p>
  <div class="crest">
    <div class="crest-ring"></div>
    <span class="crest-name">Drunavic</span>
  </div>
  <p class="vintage">2014</p>
  <p class="brand-name">Drunavic</p>
  <p class="descriptor">Orange-flavouredliqueur</p>
  <p class="appellation">INDICAZIONE GEOGRAFICA TIPICA</p>
  <div class="facts">
    <span class="abv">12% alc./vol.</span>
    <span class="style">White Wine</span>
    <span class="volume">750ml</span>
  </div>
</section>

</body>
</html>
```